Business cards for Remote DBA team

Business cards for team offering database administration, consultation, machine learning and AI services. As of now team is using both
www.korvilnet.cz and www.brestmoorlab.cz URLs

Target Market(s)

IT managers

Industry/Entity Type

It Professional

Contact Information for Business Card

Should include logo
name, email, phone, twitter tag

Font styles to use
Sans Serif

Colors

Designer to choose colors to be used in the design.

```html
<!DOCTYPE html>
<html lang="en">
<head>
<meta charset="utf-8">
<title>Korvilnet – Business Cards</title>
<link href="https://fonts.googleapis.com/css2?family=Montserrat:wght@400;500;700&display=swap" rel="stylesheet">
<style>
  :root {
    --brand-blue: #1a8ac7;
    --ink-grey: #6f7478;
    --card-white: #ffffff;
    --backdrop: #e9ebed;
    --divider: #1a8ac7;
  }
  * { box-sizing: border-box; margin: 0; padding: 0; }
  html, body { width: 1200px; height: 880px; overflow: hidden; }
  body {
    background: var(--backdrop);
    font-family: "Montserrat", Arial, sans-serif;
    position: relative;
  }
  .card {
    position: absolute;
    width: 600px;
    height: 340px;
    background: var(--card-white);
    border-radius: 22px;
    overflow: hidden;
    box-shadow: 0 10px 28px rgba(0,0,0,0.18);
  }
  .card--front { left: 80px; top: 80px; }
  .card--back { left: 520px; top: 470px; }

  .wordmark {
    position: absolute;
    display: flex;
    align-items: center;
    gap: 14px;
    color: var(--brand-blue);
    font-weight: 700;
    line-height: 1;
    white-space: nowrap;
  }
  .wordmark__dot {
    border-radius: 50%;
    background: var(--brand-blue);
    flex: none;
  }
  .card--front .wordmark { left: 50%; top: 50%; transform: translate(-50%, -50%); font-size: 48px; }
  .card--front .wordmark__dot { width: 34px; height: 34px; }
  .card--back .wordmark { left: 56px; top: 148px; font-size: 30px; gap: 10px; }
  .card--back .wordmark__dot { width: 22px; height: 22px; }

  .divider {
    position: absolute;
    left: 300px;
    top: 50px;
    width: 1.5px;
    height: 170px;
    background: var(--divider);
  }
  .contact {
    position: absolute;
    left: 330px;
    top: 44px;
    color: var(--ink-grey);
    font-size: 13px;
    line-height: 1.45;
  }
  .contact__name { color: var(--brand-blue); font-weight: 700; font-size: 22px; line-height: 1.1; }
  .contact__role { font-size: 13px; margin-bottom: 12px; }
  .contact__address { margin-bottom: 10px; }
  .contact__row { display: flex; align-items: center; gap: 8px; }
  .contact__row svg { flex: none; }
  .social-dot { width: 10px; height: 10px; border-radius: 50%; background: var(--brand-blue); margin: 0 1px; flex: none; }

  .url-band {
    position: absolute;
    left: 0; right: 0;
    top: 258px;
    height: 48px;
    background: var(--brand-blue);
    color: var(--card-white);
    display: flex;
    align-items: center;
    justify-content: center;
    font-size: 15px;
    font-weight: 500;
    letter-spacing: 2px;
  }
  .url-band__sep { margin: 0 14px; }
</style>
</head>
<body>
  <section class="card card--front" aria-label="Business card front">
    <div class="wordmark">
      <span class="wordmark__dot"></span>
      <span>Korvilnet</span>
    </div>
  </section>

  <section class="card card--back" aria-label="Business card back">
    <div class="wordmark">
      <span class="wordmark__dot"></span>
      <span>Korvilnet</span>
    </div>
    <div class="divider"></div>
    <div class="contact">
      <p class="contact__name">Tomas Lerch</p>
      <p class="contact__role">Director</p>
      <p class="contact__address">PO BOX 48, Harbour Lane<br>2nd street Ashcombe</p>
      <p class="contact__row">
        <svg width="12" height="12" viewBox="0 0 24 24" aria-hidden="true"><path fill="#1a8ac7" d="M6.6 10.8a15.1 15.1 0 0 0 6.6 6.6l2.2-2.2c.3-.3.7-.4 1-.2 1.1.4 2.3.6 3.6.6.6 0 1 .4 1 1V20c0 .6-.4 1-1 1A17 17 0 0 1 3 4c0-.6.4-1 1-1h3.5c.6 0 1 .4 1 1 0 1.3.2 2.5.6 3.6.1.3 0 .7-.2 1z"/></svg>
        (555) 318 2046
      </p>
      <p class="contact__row">
        <svg width="12" height="12" viewBox="0 0 24 24" aria-hidden="true"><rect x="2" y="5" width="20" height="14" rx="1.5" fill="#1a8ac7"/><path d="M3 6l9 7 9-7" fill="none" stroke="#fff" stroke-width="1.8"/></svg>
        info@korvilnet.cz
      </p>
      <p class="contact__row"><span class="social-dot"></span>@korvilnet</p>
    </div>
    <div class="url-band">
      <span>www.korvilnet.cz</span><span class="url-band__sep">|</span><span>www.brestmoorlab.cz</span>
    </div>
  </section>
</body>
</html>
```